Beer can label design for 12oz cans

we want a clean easy to read label we will be changing the colors to coordinate with the name change of the beer but want everyone to know what they are looking at in regards to the type of beer and us as a brewery. we are in Alaska and i picture a orange red blue green and maybe yellow color to make it clear what beer they are buying. it will be going on a 12oz can. wold like the logo to be 1 color like a dark grey maybe a weatherd look at angle maybe just to give it a little character. needs to have BIG LAKE, AK on the top or the label also needs to have made in alaska somewhere on there. there are lots of rules here are some designs i reallylike also. we are on a lake and look at north americas tallest mountain, Denali Moutain.

Target Market(s)

beer drinkers, want a recognizable can thats easy to decipher the beer type

Industry/Entity Type

drink branding.

Requirements
Must have
• this will be call the "Cold Ox" its a double IPA needs to have the appropriate letter sizes and requirements for a label
Nice to have
• want it to be clean but pop also

```html
<!DOCTYPE html>
<html lang="en">
<head>
<meta charset="utf-8">
<title>Cold Ox Double IPA – Can Label</title>
<link href="https://fonts.googleapis.com/css2?family=Abril+Fatface&family=Oswald:wght@500;600;700&display=swap" rel="stylesheet">
<style>
  :root {
    --page-bg: #f4f4f2;
    --label-yellow: #f8ec12;
    --label-band: #faf04a;
    --label-pale: #fbf58c;
    --ink: #3d3d3f;
    --rule: #c9bf10;
  }
  * { box-sizing: border-box; margin: 0; padding: 0; }
  html, body { width: 1200px; height: 1000px; overflow: hidden; }
  body {
    background: var(--page-bg);
    position: relative;
    font-family: "Oswald", sans-serif;
    color: var(--ink);
  }
  .can-label {
    position: absolute;
    left: 100px;
    top: 265px;
    width: 1000px;
    height: 470px;
    background: var(--label-yellow);
    border-radius: 18px;
    overflow: hidden;
  }
  .label-band {
    position: absolute;
    inset: 0;
    width: 100%;
    height: 100%;
  }
  .label-header {
    position: absolute;
    top: 28px;
    left: 0;
    right: 0;
    display: flex;
    align-items: flex-start;
    gap: 28px;
  }
  .header-rule {
    flex: 1;
    height: 1px;
    margin-top: 14px;
    background: var(--rule);
  }
  .brewery-mark {
    flex: none;
    text-align: center;
    white-space: nowrap;
  }
  .brewery-name {
    font-weight: 700;
    font-size: 24px;
    letter-spacing: 1px;
    line-height: 1;
  }
  .brewery-location {
    margin-top: 6px;
    font-weight: 600;
    font-size: 11px;
    letter-spacing: 2px;
    line-height: 1;
  }
  .beer-title {
    position: absolute;
    top: 168px;
    left: 0;
    width: 100%;
    text-align: center;
  }
  .beer-name {
    font-family: "Abril Fatface", serif;
    font-size: 104px;
    line-height: 1;
  }
  .beer-style {
    margin-top: 4px;
    padding-left: 150px;
    font-weight: 600;
    font-size: 27px;
    letter-spacing: 1px;
    line-height: 1;
  }
  .mountain-art {
    position: absolute;
    left: 0;
    right: 0;
    bottom: 0;
    height: 185px;
    background: linear-gradient(180deg, var(--label-yellow) 0%, var(--label-band) 35%, var(--label-pale) 100%);
  }
  .label-footer {
    position: absolute;
    left: 0;
    width: 100%;
    text-align: center;
    font-weight: 600;
    line-height: 1;
  }
  .made-in {
    top: 414px;
    font-size: 13px;
    letter-spacing: 0.5px;
  }
  .volume {
    top: 442px;
    font-size: 10px;
  }
</style>
</head>
<body>
  <section class="can-label" aria-label="Cold Ox Double IPA can label">
    <svg class="label-band" viewBox="0 0 1000 470" preserveAspectRatio="none" aria-hidden="true">
      <polygon points="0,175 1000,40 1000,300 0,300" fill="var(--label-band)"/>
    </svg>

    <div class="mountain-art" role="img" aria-label="Illustration of Denali mountain range across the lower label"></div>

    <header class="label-header">
      <div class="header-rule"></div>
      <div class="brewery-mark">
        <p class="brewery-name">TUNDRA LAKE BREWING CO.</p>
        <p class="brewery-location">BIG LAKE, ALASKA</p>
      </div>
      <div class="header-rule"></div>
    </header>

    <div class="beer-title">
      <h1 class="beer-name">Cold Ox</h1>
      <p class="beer-style">DOUBLE IPA</p>
    </div>

    <p class="label-footer made-in">MADE IN ALASKA</p>
    <p class="label-footer volume">12oz</p>
  </section>
</body>
</html>
```